Volusion Pet Store Web Template

We need a new web design for an online Pet Store based in Australia but looking to expand internationally in the future.

The template HTML & CSS should be easily integrated into a volusion web-store.

We sell a wide range of high quality pet products to our customers at competitive prices.This is our unique selling point.

We intend to become a market leader hence our brand has to look the part with simple yet outstanding icons.

The overall design has to be more visually appealing and simpler than our competitors and lead to a higher conversion rate.

The following are our biggest competitors:
www.mossfold.com.au
www.grovewick.com.au
www.tidlowe.com.au

Of our competitors www.tidlowe.com.au has the feel that we intend to have but obviously it has to be unique & iconic.

In short our web design has to be associated with Leading,Trust & Quality.
Updates

Please find attached Logo so that the site color theme can blend with the logo.

Target Market(s)

Online Pet Products shoppers worldwide

Industry/Entity Type

Pet

Coding

Coded - Design and coding required

Number of Pages Required

3 page

Font styles to use
Sans Serif

Requirements
Must have
• Check out page design.
• Product description menus(when you click on the product)
• Categories should be the same and should be hid or un-hidden by admin.
• Color theme will depend on the final logo to be completed soon.
Nice to have
• Please find attached logo.The site should blend well with logo.

```html
<!DOCTYPE html>
<html lang="en">
<head>
<meta charset="utf-8">
<title>Pet Store</title>
<link rel="stylesheet" href="https://fonts.googleapis.com/css2?family=Roboto:wght@300;400;500;700&display=swap">
<style>
:root{
  --orange:#fe980f;
  --cyan:#00bff3;
  --ink:#363432;
  --muted:#696763;
  --line:#ececec;
  --bar:#f0f0e9;
  --btn:#f0f0e9;
  --white:#ffffff;
}
*{box-sizing:border-box;margin:0;padding:0}
html,body{width:1200px;height:2654px;overflow:hidden}
body{position:relative;background:var(--white);font-family:'Roboto',Arial,sans-serif;color:var(--ink)}
.abs{position:absolute}
a{color:inherit;text-decoration:none}

/* top bar */
.topbar{left:0;top:0;width:1200px;height:28px;background:var(--bar);font-size:11px;color:var(--muted)}
.topbar .contact{left:94px;top:7px;display:flex;gap:18px}
.topbar .contact span{display:flex;align-items:center;gap:5px}
.topbar .social{right:90px;top:8px;display:flex;gap:26px}
.topbar .social i{display:block;width:11px;height:11px;border-radius:50%;background:#8a8a86}

/* header */
.brand{left:94px;top:52px;display:flex;align-items:center;gap:8px;font-size:25px;font-weight:700;color:var(--orange)}
.brand .mark{width:28px;height:28px;background:var(--orange);border-radius:4px}
.header-rule{left:94px;top:100px;width:1016px;height:1px;background:var(--line)}
.account-menu{left:0;width:1200px;top:111px;display:flex;justify-content:center;gap:22px;font-size:12px;color:var(--muted)}
.account-menu span{display:flex;align-items:center;gap:5px}
.main-nav{left:94px;top:154px;display:flex;gap:25px;font-size:15px;font-weight:300;color:var(--muted)}
.main-nav .active{color:var(--orange)}
.search{left:971px;top:153px;width:139px;height:30px;background:var(--bar);font-size:11px;color:#b5b5b0;padding:8px 10px;display:flex;justify-content:space-between;align-items:center}

/* hero */
.hero-arrow{top:432px;width:20px;height:34px}
.hero-brand{left:195px;top:316px;display:flex;align-items:center;gap:10px;font-size:48px;font-weight:700;color:var(--orange)}
.hero-brand .mark{width:50px;height:50px;border-radius:8px;background:var(--orange)}
.hero-tagline{left:195px;top:381px;font-size:25px;font-weight:700;color:var(--ink)}
.hero-copy{left:195px;top:425px;width:430px;font-size:14px;line-height:21px;color:var(--muted);font-weight:300}
.hero-btn{left:195px;top:499px;width:80px;height:30px;background:var(--orange);color:#fff;font-size:13px;display:flex;align-items:center;justify-content:center}
.hero-photo{left:671px;top:213px;width:394px;height:382px;background:radial-gradient(circle at 55% 60%,#d8d6d2 0%,#c9b79a 40%,#f2eee8 72%,#ffffff 100%)}
.hero-dots{left:584px;top:565px;display:flex;gap:4px}
.hero-dots i{width:7px;height:7px;border-radius:50%;background:#c4c4c0}
.hero-dots i.on{background:var(--orange)}

/* section titles */
.section-title{height:20px;display:flex;align-items:center;justify-content:center;font-size:15px;font-weight:700;color:var(--orange);text-transform:uppercase}
.section-title::before,.section-title::after{content:"";flex:1;height:1px;background:var(--line);margin:0 14px}
.section-title.wide::before,.section-title.wide::after{margin:0 22px}

/* sidebar */
.side-panel{border:1px solid #f7f7f0}
.category-list{left:94px;top:689px;width:233px;height:317px;padding:18px 18px 0 18px;list-style:none}
.category-list li{height:29px;font-size:11.5px;font-weight:500;color:var(--muted);display:flex;justify-content:space-between;align-items:center}
.category-list li b{font-size:15px;font-weight:400;color:#8c8c88}
.price-box{left:94px;top:1083px;width:233px;height:85px}
.price-box .track{left:34px;top:26px;width:163px;height:9px;border-radius:5px;background:#f5f5f5;border:1px solid #e6e6e6}
.price-box .fill{left:100px;top:26px;width:48px;height:9px;background:var(--orange);border-radius:5px}
.price-box .knob{top:22px;width:16px;height:16px;border-radius:50%;background:#f5f5f5;border:1px solid #cfcfcf}
.price-box .lbl{top:53px;font-size:11px;font-weight:700;color:var(--ink)}
.ad-cap{left:94px;width:233px;height:17px;background:#eeeeee}
.promo-banner{left:94px;top:1219px;width:233px;height:293px;background:linear-gradient(180deg,#ffffff 0%,#f6eeee 30%,#c89a72 55%,#8a5a36 80%,#d9c6a8 100%)}
.kitten-photo{left:94px;top:1580px;width:233px;height:278px;background:linear-gradient(160deg,#ffffff 0%,#d8b48a 45%,#9c7654 80%,#ffffff 100%)}

/* product cards */
.card{position:absolute;border:1px solid #f4f4ef;background:#fff;text-align:center}
.card .photo{position:absolute;left:22px;right:22px;border-radius:4px}
.card .price{position:absolute;left:0;right:0;font-size:23px;font-weight:700;color:var(--orange)}
.card .name{position:absolute;left:0;right:0;font-size:12px;color:var(--muted)}
.card .btn-cart{position:absolute;left:50%;transform:translateX(-50%);height:28px;padding:0 13px;background:var(--btn);display:flex;align-items:center;gap:5px;font-size:12px;color:var(--muted);white-space:nowrap}
.card .actions{position:absolute;left:0;right:0;bottom:0;height:48px;border-top:1px solid var(--line);display:flex;justify-content:space-around;align-items:center;padding:0 8px;font-size:10px;color:#b3b3ae}
.card .actions span{display:flex;align-items:center;gap:4px}
.card .actions i{width:9px;height:9px;background:#c7c7c2;display:block}
.ribbon{position:absolute;top:-1px;right:-1px;width:38px;height:38px;clip-path:polygon(0 0,100% 0,100% 100%)}
.ribbon.new{background:#fe4a3a}
.ribbon.sale{background:#2fbf6a}

.feature .photo{top:10px;height:190px}
.feature .price{top:228px}
.feature .name{top:266px}
.feature .btn-cart{top:290px}

.tab-card .photo{left:16px;right:16px;top:10px;height:150px}
.tab-card .price{top:168px}
.tab-card .name{top:204px}
.tab-card .btn-cart{top:230px}

.rec .photo{top:8px;height:110px}
.rec .price{top:122px}
.rec .name{top:163px}
.rec .btn-cart{top:192px}

.tabs{left:367px;top:1496px;width:743px;height:36px;background:var(--cyan);display:flex;font-size:12px;color:#fff}
.tabs span{padding:0 13px;display:flex;align-items:center}
.tabs .on{background:var(--orange)}
.carousel-arrow{width:24px;height:24px;background:var(--orange);display:flex;align-items:center;justify-content:center;z-index:2}

/* footer */
.footer{left:0;top:2185px;width:1200px;height:437px;background:var(--cyan);color:#fff}
.footer .brand-foot{left:94px;top:55px;display:flex;align-items:center;gap:6px;font-size:22px;font-weight:700;color:var(--orange)}
.footer .brand-foot .mark{width:24px;height:24px;background:var(--orange);border-radius:3px}
.footer .thumb{top:52px;width:119px;height:53px}
.footer .map{left:875px;top:25px;width:235px;height:115px;background:radial-gradient(ellipse at 50% 50%,rgba(255,255,255,.28) 0%,rgba(255,255,255,.12) 55%,rgba(255,255,255,0) 75%)}
.footer .address{left:896px;top:75px;width:200px;font-size:11px;line-height:16px;color:#e6f8fe}
.footer .rule{left:80px;top:167px;width:1042px;height:1px;background:rgba(255,255,255,.85)}
.footer .col{top:201px}
.footer .col h4{font-size:13px;font-weight:700;text-transform:uppercase;margin-bottom:18px}
.footer .col ul{list-style:none}
.footer .col li{font-size:11.5px;height:28.5px;color:#f2fbff}
.footer .newsletter{left:875px;top:202px;display:flex}
.footer .newsletter .field{width:186px;height:31px;background:#fff}
.footer .newsletter .go{width:49px;height:31px;background:var(--orange);display:flex;align-items:center;justify-content:center}
.bottombar{left:0;top:2622px;width:1200px;height:32px;background:#d6d6d6;font-size:11px;color:var(--muted);padding:10px 94px}
</style>
</head>
<body>

<div class="topbar abs">
  <div class="contact abs">
    <span><svg width="10" height="10" viewBox="0 0 10 10"><path d="M2 1l2 2-1 1.5c.6 1.2 1.3 1.9 2.5 2.5L7 6l2 2-1.5 1.5C4.5 9 1 5.5.5 2.5z" fill="#696763"/></svg>+1 555 01 23 456</span>
    <span><svg width="11" height="8" viewBox="0 0 11 8"><rect width="11" height="8" fill="#696763"/><path d="M0 0l5.5 4.5L11 0" stroke="#f0f0e9" fill="none"/></svg>info@pawnestshop.com</span>
  </div>
  <div class="social abs"><i></i><i></i><i></i><i></i></div>
</div>

<div class="brand abs"><span class="mark"></span>Pet Store</div>
<div class="header-rule abs"></div>

<nav class="account-menu abs">
  <span><svg width="9" height="10" viewBox="0 0 9 10"><circle cx="4.5" cy="3" r="2.5" fill="#696763"/><path d="M0 10c0-3 2-4.5 4.5-4.5S9 7 9 10z" fill="#696763"/></svg>Account</span>
  <span><svg width="10" height="10" viewBox="0 0 10 10"><path d="M5 0l1.5 3.3 3.5.4-2.6 2.4.7 3.5L5 7.8 1.9 9.6l.7-3.5L0 3.7l3.5-.4z" fill="#696763"/></svg>Wishlist</span>
  <span><svg width="10" height="10" viewBox="0 0 10 10"><path d="M5 0l2 2-2 2-2-2zM5 6l2 2-2 2-2-2zM0 5l2-2 2 2-2 2zM6 5l2-2 2 2-2 2z" fill="#696763"/></svg>Checkout</span>
  <span><svg width="11" height="10" viewBox="0 0 11 10"><path d="M0 0h2l.5 2H11l-1.5 4.5H3L1.5 1H0z" fill="#696763"/><circle cx="4" cy="8.5" r="1.2" fill="#696763"/><circle cx="8.5" cy="8.5" r="1.2" fill="#696763"/></svg>Cart</span>
  <span><svg width="9" height="10" viewBox="0 0 9 10"><rect y="4.5" width="9" height="5.5" fill="#696763"/><path d="M2 4.5V3a2.5 2.5 0 0 1 5 0v1.5" stroke="#696763" fill="none" stroke-width="1.3"/></svg>Login</span>
</nav>

<nav class="main-nav abs">
  <span class="active">Dog</span><span>Cat</span><span>Fish</span><span>Reptile</span><span>Small Animal</span>
</nav>
<div class="search abs">Search<svg width="10" height="10" viewBox="0 0 10 10"><circle cx="4" cy="4" r="3" stroke="#8c8c88" fill="none" stroke-width="1.4"/><path d="M6.2 6.2L9.5 9.5" stroke="#8c8c88" stroke-width="1.4"/></svg></div>

<!-- hero slider -->
<svg class="hero-arrow abs" style="left:92px" viewBox="0 0 20 34"><path d="M17 2L3 17l14 15" stroke="#b3b3ae" stroke-width="3" fill="none"/></svg>
<svg class="hero-arrow abs" style="left:1088px" viewBox="0 0 20 34"><path d="M3 2l14 15L3 32" stroke="#b3b3ae" stroke-width="3" fill="none"/></svg>
<div class="hero-brand abs"><span class="mark"></span>Pet Store</div>
<div class="hero-tagline abs">Your confidence pet store</div>
<p class="hero-copy abs">Nemo enim ipsam voluptatem quia voluptas sit aspernatur aut odit aut fugit, sed quia consequuntur magni dolores.</p>
<a class="hero-btn abs">Buy now!</a>
<div class="hero-photo abs" role="img" aria-label="A grey parrot perched on a pet carrier with a cat inside and a small dog beside it"></div>
<div class="hero-dots abs"><i></i><i class="on"></i><i></i></div>

<!-- sidebar -->
<div class="section-title abs" style="left:94px;top:643px;width:233px">Products</div>
<ul class="category-list side-panel abs">
  <li>PREMIUM FOOD<b>+</b></li><li>HEALTH CARE<b>+</b></li><li>FLEA CONTROL<b>+</b></li>
  <li>TOYS</li><li>FASHION</li><li>ACCESSORIES</li><li>SPORT</li><li>CLOTHING</li><li>BEDDING</li><li>CLEAN UP</li>
</ul>
<div class="section-title abs" style="left:94px;top:1037px;width:233px">Price Range</div>
<div class="price-box side-panel abs">
  <div class="track abs"></div>
  <div class="fill abs"></div>
  <div class="knob abs" style="left:94px"></div>
  <div class="knob abs" style="left:140px"></div>
  <div class="lbl abs" style="left:34px">$ 0</div>
  <div class="lbl abs" style="left:167px">$ 600</div>
</div>
<div class="ad-cap abs" style="top:1202px"></div>
<div class="promo-banner abs" role="img" aria-label="Promotional banner announcing free shipping on orders over $50, with a cat resting on a wooden chair"></div>
<div class="ad-cap abs" style="top:1548px"></div>
<div class="kitten-photo abs" role="img" aria-label="Two tabby kittens sitting side by side"></div>

<!-- features -->
<div class="section-title wide abs" style="left:367px;top:643px;width:743px">Features Items</div>

<div class="card feature" style="left:367px;top:689px;width:236px;height:388px">
  <div class="photo" role="img" aria-label="Yellow and green pet bathing brushes" style="background:radial-gradient(circle,#c8e05a 0%,#f2f4e0 60%,#fff 100%)"></div>
  <div class="price">$26</div><div class="name">Tub Nub Bathing Brushn</div>
  <div class="btn-cart"><svg width="11" height="10" viewBox="0 0 11 10"><path d="M0 0h2l.5 2H11l-1.5 4.5H3L1.5 1H0z" fill="#696763"/><circle cx="4" cy="8.5" r="1.2" fill="#696763"/><circle cx="8.5" cy="8.5" r="1.2" fill="#696763"/></svg>Add to cart</div>
  <div class="actions"><span><i></i>Add to wishlist</span><span><i></i>Add to compare</span></div>
</div>
<div class="card feature" style="left:620px;top:689px;width:236px;height:388px">
  <div class="photo" role="img" aria-label="Woven pet carry bed with a small dog" style="background:radial-gradient(circle,#d9bf88 0%,#f3ecdc 60%,#fff 100%)"></div>
  <div class="price">$56</div><div class="name">Soft Bed</div>
  <div class="btn-cart"><svg width="11" height="10" viewBox="0 0 11 10"><path d="M0 0h2l.5 2H11l-1.5 4.5H3L1.5 1H0z" fill="#696763"/><circle cx="4" cy="8.5" r="1.2" fill="#696763"/><circle cx="8.5" cy="8.5" r="1.2" fill="#696763"/></svg>Add to cart</div>
  <div class="actions"><span><i></i>Add to wishlist</span><span><i></i>Add to compare</span></div>
</div>
<div class="card feature" style="left:874px;top:689px;width:236px;height:388px">
  <div class="photo" role="img" aria-label="Teal bottle of pet conditioning shampoo" style="background:radial-gradient(circle,#3cb8b0 0%,#e3f4f2 55%,#fff 100%)"></div>
  <div class="price">$6</div><div class="name">Conditioning Shampoo</div>
  <div class="btn-cart"><svg width="11" height="10" viewBox="0 0 11 10"><path d="M0 0h2l.5 2H11l-1.5 4.5H3L1.5 1H0z" fill="#696763"/><circle cx="4" cy="8.5" r="1.2" fill="#696763"/><circle cx="8.5" cy="8.5" r="1.2" fill="#696763"/></svg>Add to cart</div>
  <div class="actions"><span><i></i>Add to wishlist</span><span><i></i>Add to compare</span></div>
</div>

<div class="card feature" style="left:367px;top:1093px;width:236px;height:388px">
  <span class="ribbon new"></span>
  <div class="photo" role="img" aria-label="Red jar of pet supplement" style="background:radial-gradient(circle,#c83a40 0%,#f1dadb 55%,#fff 100%)"></div>
  <div class="price">$56</div><div class="name">Thing for pet</div>
  <div class="btn-cart"><svg width="11" height="10" viewBox="0 0 11 10"><path d="M0 0h2l.5 2H11l-1.5 4.5H3L1.5 1H0z" fill="#696763"/><circle cx="4" cy="8.5" r="1.2" fill="#696763"/><circle cx="8.5" cy="8.5" r="1.2" fill="#696763"/></svg>Add to cart</div>
  <div class="actions"><span><i></i>Add to wishlist</span><span><i></i>Add to compare</span></div>
</div>
<div class="card feature" style="left:620px;top:1093px;width:236px;height:388px">
  <span class="ribbon sale"></span>
  <div class="photo" role="img" aria-label="Navy drawstring pet sleeping sack" style="background:radial-gradient(circle,#2a3f72 0%,#dde2ee 58%,#fff 100%)"></div>
  <div class="price">$56</div><div class="name">Thing for pet</div>
  <div class="btn-cart"><svg width="11" height="10" viewBox="0 0 11 10"><path d="M0 0h2l.5 2H11l-1.5 4.5H3L1.5 1H0z" fill="#696763"/><circle cx="4" cy="8.5" r="1.2" fill="#696763"/><circle cx="8.5" cy="8.5" r="1.2" fill="#696763"/></svg>Add to cart</div>
  <div class="actions"><span><i></i>Add to wishlist</span><span><i></i>Add to compare</span></div>
</div>
<div class="card feature" style="left:874px;top:1093px;width:236px;height:388px">
  <div class="photo" role="img" aria-label="Black and steel pet food bowl" style="background:radial-gradient(ellipse,#5a5a5a 0%,#d4d4d4 50%,#fff 100%)"></div>
  <div class="price">$56</div><div class="name">Thing for pet</div>
  <div class="btn-cart"><svg width="11" height="10" viewBox="0 0 11 10"><path d="M0 0h2l.5 2H11l-1.5 4.5H3L1.5 1H0z" fill="#696763"/><circle cx="4" cy="8.5" r="1.2" fill="#696763"/><circle cx="8.5" cy="8.5" r="1.2" fill="#696763"/></svg>Add to cart</div>
  <div class="actions"><span><i></i>Add to wishlist</span><span><i></i>Add to compare</span></div>
</div>

<!-- category tabs -->
<div class="tabs abs">
  <span class="on">FOOD</span><span>BOWLS &amp; FEEDERS</span><span>CARRIERS &amp; CAGES</span><span>GROOMING SUPPLIES</span><span>HEALTH CARE</span>
</div>
<div class="card tab-card" style="left:367px;top:1560px;width:165px;height:281px">
  <div class="photo" role="img" aria-label="Red and black pet collar" style="background:radial-gradient(circle,#7a3a2a 0%,#eee3df 55%,#fff 100%)"></div>
  <div class="price">$16</div><div class="name">Thing for pet</div>
  <div class="btn-cart"><svg width="11" height="10" viewBox="0 0 11 10"><path d="M0 0h2l.5 2H11l-1.5 4.5H3L1.5 1H0z" fill="#696763"/><circle cx="4" cy="8.5" r="1.2" fill="#696763"/><circle cx="8.5" cy="8.5" r="1.2" fill="#696763"/></svg>Add to cart</div>
</div>
<div class="card tab-card" style="left:560px;top:1560px;width:165px;height:281px">
  <div class="photo" role="img" aria-label="Yellow tub of turtle food" style="background:radial-gradient(circle,#e0b820 0%,#f6efd0 55%,#fff 100%)"></div>
  <div class="price">$16</div><div class="name">Thing for pet</div>
  <div class="btn-cart"><svg width="11" height="10" viewBox="0 0 11 10"><path d="M0 0h2l.5 2H11l-1.5 4.5H3L1.5 1H0z" fill="#696763"/><circle cx="4" cy="8.5" r="1.2" fill="#696763"/><circle cx="8.5" cy="8.5" r="1.2" fill="#696763"/></svg>Add to cart</div>
</div>
<div class="card tab-card" style="left:753px;top:1560px;width:165px;height:281px">
  <div class="photo" role="img" aria-label="Glass reptile terrarium" style="background:radial-gradient(circle,#8a6a48 0%,#e8e0d6 55%,#fff 100%)"></div>
  <div class="price">$16</div><div class="name">Thing for pet</div>
  <div class="btn-cart"><svg width="11" height="10" viewBox="0 0 11 10"><path d="M0 0h2l.5 2H11l-1.5 4.5H3L1.5 1H0z" fill="#696763"/><circle cx="4" cy="8.5" r="1.2" fill="#696763"/><circle cx="8.5" cy="8.5" r="1.2" fill="#696763"/></svg>Add to cart</div>
</div>
<div class="card tab-card" style="left:946px;top:1560px;width:165px;height:281px">
  <div class="photo" role="img" aria-label="Round fish bowl with green plants" style="background:radial-gradient(circle,#4a9a4a 0%,#dcefdc 55%,#fff 100%)"></div>
  <div class="price">$16</div><div class="name">Thing for pet</div>
  <div class="btn-cart"><svg width="11" height="10" viewBox="0 0 11 10"><path d="M0 0h2l.5 2H11l-1.5 4.5H3L1.5 1H0z" fill="#696763"/><circle cx="4" cy="8.5" r="1.2" fill="#696763"/><circle cx="8.5" cy="8.5" r="1.2" fill="#696763"/></svg>Add to cart</div>
</div>

<!-- recommended -->
<div class="section-title wide abs" style="left:367px;top:1866px;width:743px">Recommended Items</div>
<div class="card rec" style="left:367px;top:1912px;width:236px;height:245px">
  <div class="photo" role="img" aria-label="Bags of pet treats" style="background:radial-gradient(circle,#c8a030 0%,#f3ead0 55%,#fff 100%)"></div>
  <div class="price">$22</div><div class="name">Thing for pet</div>
  <div class="btn-cart"><svg width="11" height="10" viewBox="0 0 11 10"><path d="M0 0h2l.5 2H11l-1.5 4.5H3L1.5 1H0z" fill="#696763"/><circle cx="4" cy="8.5" r="1.2" fill="#696763"/><circle cx="8.5" cy="8.5" r="1.2" fill="#696763"/></svg>Add to cart</div>
</div>
<div class="card rec" style="left:620px;top:1912px;width:236px;height:245px">
  <div class="photo" role="img" aria-label="Range of dry pet food bags" style="background:radial-gradient(ellipse,#b83040 0%,#eed8dc 55%,#fff 100%)"></div>
  <div class="price">$22</div><div class="name">Thing for pet</div>
  <div class="btn-cart"><svg width="11" height="10" viewBox="0 0 11 10"><path d="M0 0h2l.5 2H11l-1.5 4.5H3L1.5 1H0z" fill="#696763"/><circle cx="4" cy="8.5" r="1.2" fill="#696763"/><circle cx="8.5" cy="8.5" r="1.2" fill="#696763"/></svg>Add to cart</div>
</div>
<div class="card rec" style="left:874px;top:1912px;width:236px;height:245px">
  <div class="photo" role="img" aria-label="Boxes of flea treatment" style="background:radial-gradient(ellipse,#7a4aa0 0%,#e8dcef 55%,#fff 100%)"></div>
  <div class="price">$22</div><div class="name">Thing for pet</div>
  <div class="btn-cart"><svg width="11" height="10" viewBox="0 0 11 10"><path d="M0 0h2l.5 2H11l-1.5 4.5H3L1.5 1H0z" fill="#696763"/><circle cx="4" cy="8.5" r="1.2" fill="#696763"/><circle cx="8.5" cy="8.5" r="1.2" fill="#696763"/></svg>Add to cart</div>
</div>
<div class="carousel-arrow abs" style="left:354px;top:2024px"><svg width="8" height="10" viewBox="0 0 8 10"><path d="M6 1L2 5l4 4" stroke="#fff" stroke-width="2" fill="none"/></svg></div>
<div class="carousel-arrow abs" style="left:1098px;top:2024px"><svg width="8" height="10" viewBox="0 0 8 10"><path d="M2 1l4 4-4 4" stroke="#fff" stroke-width="2" fill="none"/></svg></div>

<!-- footer -->
<footer class="footer abs">
  <div class="brand-foot abs"><span class="mark"></span>Pet Store</div>
  <div class="thumb abs" style="left:280px;background:linear-gradient(135deg,#3a8a2a,#e0b020)" role="img" aria-label="Parrot among green leaves"></div>
  <div class="thumb abs" style="left:426px;background:linear-gradient(135deg,#6a8a3a,#1e1a14)" role="img" aria-label="Black puppies on grass"></div>
  <div class="thumb abs" style="left:571px;background:linear-gradient(135deg,#9a8a7a,#e0d2c2)" role="img" aria-label="Cat lying on a deck"></div>
  <div class="thumb abs" style="left:715px;background:linear-gradient(135deg,#4a7a2a,#b86a2a)" role="img" aria-label="Guinea pig on grass"></div>
  <div class="map abs" role="img" aria-label="Faint world map"></div>
  <div class="address abs">18 Harbour Lane Sidney Beach,<br>Australia</div>
  <div class="rule abs"></div>
  <div class="col abs" style="left:94px"><h4>Shop Online</h4><ul><li>Online Help</li><li>Contact Us</li><li>Order Status</li><li>Change Location</li><li>FAQ’s</li></ul></div>
  <div class="col abs" style="left:266px"><h4>Pet Services</h4><ul><li>Dogs</li><li>Cats</li><li>Fish</li><li>Small Animal</li><li>Gift Cards</li></ul></div>
  <div class="col abs" style="left:440px"><h4>Policies</h4><ul><li>Terms of Use</li><li>Privacy Policy</li><li>Refund Policy</li><li>Billing System</li><li>Ticket System</li></ul></div>
  <div class="col abs" style="left:614px"><h4>More Information</h4><ul><li>Company Information</li><li>Careers</li><li>Store Location</li><li>Affiliate Program</li><li>Copyright</li></ul></div>
  <div class="newsletter abs"><div class="field"></div><div class="go"><svg width="14" height="14" viewBox="0 0 14 14"><circle cx="7" cy="7" r="6" stroke="#fff" stroke-width="1.6" fill="none"/><path d="M4 7h6M7.5 4.5L10 7l-2.5 2.5" stroke="#fff" stroke-width="1.6" fill="none"/></svg></div></div>
</footer>
<div class="bottombar abs">Copyright © 2014 PetStore Inc. All rights reserved.</div>

</body>
</html>
```